依頼詳細
デザインの依頼内容は、「ひなた夢みるバー」というアイスキャンディーのパッケージです。パッケージとはいっても単純な袋です。ですので主には、商品ロゴデザインとなります。

このアイスキャンディーの発売にあたっては、当店の歴史を生かしながら新しいモノチャレンジしていく姿勢も感じられるものにしたいと考えています。レトロ感・歴史などを感じられるものにしたいです。

一方でブランドを育てるにあたり、シンプルで一目でわかりやすくオシャレなデザインにしたいという思いもあります。

また、使用する食材は地元の佐野市もしくは近隣のものを主に使用します。現在佐野市では、郷土愛マーク「WE HUG KOMA」というマークを作りそれを広めることによって郷土愛を強めていく活動をしており、当店としてもその活動に賛同しており商品のデザインに入れたいと考えております。

アイスの種類は数種類発売予定です。デザイン的には基本デザインを考えて頂ければと考えております。
・ミルク系
・あずき系
・甘酒系
・フルーツ餡系
・他

【色数】単色~2色程度
基本的にはアイスの種類の数だけパッケージ印刷しなければいけないため、コストの絡みで少なく抑えます。

【添付データについて】
こちらのデータは、現在試作品販売のために作成した、社内の素人によるデータです。そして商品名は、郷土愛マーク「WE HUG KOMA」からインスパイアされた「ひなた夢みるバー」というベタなネーミングです。

佐野市は佐野ラーメンが有名ですが他に、イチゴや、重要文化財の北村蘭渓の「花鳥帖」、国指定史跡となった「鷲尾峰砦跡」、名水百選の「霧ヶ谷観音淵湧水」などの地元の誇れるものがありデザインに取り入れてあります。レトロ感を主に意識したベタなデザインです。あくまでも参考になれば、ということで添付しました。このデザインをブラッシュアップして頂くことも一考かと思います。

また、デザインにあたり森田久兵衛商店のマークを意識しました。
記載項目
【素材】PP
【袋サイズ】W85mm x H200(マチ無し)
【商品サイズ】W55mm x H100(H150棒含む) x D20mm
*ツンドラ坊やのような形状です。
【記載事項】表面:商品ロゴ等
裏面:食品としての最低限の記載、他にご提案ございましたら!
希望イメージ
シンプル 複雑
単色 カラフル
暗い 明るい
日常 高級
遊び心 厳粛
未来的 伝統的
女性的 男性的
希望する色
納品ファイル
• イラストレーター形式 (.ai)
• フォトショップ形式 (.psd)
補足説明

大変悩みました。絞り切れずレトロ感とシンプルを優先させて頂きました。

素晴らしいデザインをありがとうございます。
これからもデザインをお願いしたいと思いますので
その際にはまたご参加いただけると幸いです。

```html
<!DOCTYPE html>
<html lang="ja">
<head>
<meta charset="utf-8">
<title>ひなた夢みるバー パッケージ</title>
<link href="https://fonts.googleapis.com/css2?family=Shippori+Mincho:wght@500;700;800&family=Noto+Serif+JP:wght@400;600&display=swap" rel="stylesheet">
<style>
  :root {
    --page: #ffffff;
    --mono-ink: #231815;
    --mono-paper: #ffffff;
    --mono-soft: #d6d6d6;
    --rose-ink: #6e2b3c;
    --rose-paper: #ecdde0;
    --rose-soft: #cfaeb6;
  }
  * { box-sizing: border-box; margin: 0; padding: 0; }
  html, body { width: 677px; height: 1200px; overflow: hidden; background: var(--page); }
  body { position: relative; font-family: "Shippori Mincho", "Noto Serif JP", serif; }

  .pack {
    position: absolute; width: 260px; height: 510px;
    background: var(--paper); color: var(--ink);
    border: 1px solid var(--soft);
  }
  .pack--mono { --ink: var(--mono-ink); --paper: var(--mono-paper); --soft: var(--mono-soft); }
  .pack--rose { --ink: var(--rose-ink); --paper: var(--rose-paper); --soft: var(--rose-soft); }

  .pack__frame {
    position: absolute; inset: 10px;
    border: 2px solid var(--ink);
    outline: 1px solid var(--ink); outline-offset: -6px;
  }
  .ornament { position: absolute; background: var(--soft); border-radius: 3px; }
  .vertical { position: absolute; writing-mode: vertical-rl; white-space: nowrap; line-height: 1; }

  /* ---------- front ---------- */
  .front__maker {
    position: absolute; left: 28px; right: 28px; top: 26px; height: 30px;
    border: 1.5px solid var(--ink); background: var(--paper);
    display: flex; align-items: center; justify-content: center;
    font-size: 14px; font-weight: 700; letter-spacing: 2px;
  }
  .front__corner { width: 20px; height: 20px; border-radius: 50%; }
  .front__cloud-row { left: 28px; right: 28px; top: 64px; height: 14px; }

  .front__medal { position: absolute; left: 20px; top: 88px; width: 220px; height: 220px; color: var(--ink); }
  .front__scene { left: 85px; top: 114px; width: 90px; height: 22px; border-radius: 45px 45px 3px 3px; }
  .front__title-sub { left: 152px; top: 144px; font-size: 18px; font-weight: 700; letter-spacing: 2px; }
  .front__title-main { left: 106px; top: 150px; font-size: 40px; font-weight: 800; letter-spacing: 2px; }
  .front__title-bar { left: 82px; top: 212px; font-size: 18px; font-weight: 700; letter-spacing: 2px; }
  .front__badge {
    position: absolute; left: 160px; top: 232px; width: 36px; height: 36px;
    border-radius: 50%; background: var(--ink); opacity: .8;
  }

  .front__flavor {
    position: absolute; left: 44px; right: 44px; top: 330px; height: 30px;
    background: var(--ink); color: var(--paper);
    display: flex; align-items: center; justify-content: center;
    font-size: 15px; font-weight: 700; letter-spacing: 6px;
    clip-path: polygon(0 0, 100% 0, 94% 50%, 100% 100%, 0 100%, 6% 50%);
  }
  .front__wave { left: 28px; right: 28px; top: 376px; height: 40px; }
  .front__tagline {
    position: absolute; left: 0; right: 0; top: 428px; text-align: center;
    font-family: "Noto Serif JP", serif; font-size: 8.5px; letter-spacing: .5px;
  }
  .front__region {
    position: absolute; left: 60px; right: 60px; top: 446px; height: 28px;
    border-top: 1.5px solid var(--ink); border-bottom: 1.5px solid var(--ink);
    display: flex; align-items: center; justify-content: center;
    font-size: 15px; font-weight: 700; letter-spacing: 5px;
  }

  /* ---------- back ---------- */
  .back__cloud-top { left: 24px; right: 24px; top: 40px; height: 28px; }
  .back__cloud-bottom { left: 24px; right: 24px; top: 444px; height: 26px; }
  .back__mark { left: 26px; top: 90px; width: 26px; height: 26px; border-radius: 50%; }
  .back__seal {
    position: absolute; left: 62px; top: 82px; width: 44px; height: 44px;
    border-radius: 50%; background: var(--ink); opacity: .85;
  }
  .back__logo-sub { left: 84px; top: 140px; font-size: 11px; font-weight: 700; letter-spacing: 1px; }
  .back__logo-main { left: 66px; top: 178px; font-size: 30px; font-weight: 800; letter-spacing: 2px; }
  .back__stamp {
    position: absolute; left: 36px; top: 232px; width: 22px; height: 22px;
    border: 1.5px solid var(--ink); border-radius: 50%;
  }
  .back__stick { left: 64px; top: 364px; width: 36px; height: 58px; border-radius: 4px; }

  .back__label {
    position: absolute; left: 132px; top: 92px; width: 104px; height: 200px;
    border: 1.5px solid var(--ink);
    writing-mode: vertical-rl; padding: 6px 4px;
    font-family: "Noto Serif JP", serif; font-size: 8px; line-height: 1.55;
  }
  .back__label-kind { font-weight: 600; font-size: 9px; }
  .back__label-name {
    font-family: "Shippori Mincho", serif; font-weight: 800; font-size: 16px;
    border-left: 1px solid var(--ink); padding-left: 4px; margin-left: 4px;
  }
</style>
</head>
<body>

<!-- front, single colour -->
<section class="pack pack--mono front" style="left:45px; top:14px;">
  <div class="pack__frame"></div>
  <div class="ornament front__corner" style="left:18px; top:18px;" role="img" aria-label="角の飾り"></div>
  <div class="ornament front__corner" style="right:18px; top:18px;" role="img" aria-label="角の飾り"></div>
  <div class="front__maker">味噌まんじゅう朝霧屋</div>
  <div class="ornament front__cloud-row" role="img" aria-label="雲文様の帯"></div>
  <svg class="front__medal" viewBox="0 0 220 220" aria-hidden="true">
    <defs><path id="arcA" d="M110,110 m-97,0 a97,97 0 1,1 194,0 a97,97 0 1,1 -194,0"/></defs>
    <circle cx="110" cy="110" r="105" fill="none" stroke="currentColor" stroke-width="1.5"/>
    <circle cx="110" cy="110" r="88" fill="none" stroke="currentColor" stroke-width="1"/>
    <text font-size="8" fill="currentColor" font-family="Noto Serif JP, serif" letter-spacing="1">
      <textPath href="#arcA">Ice candy with milk and fruit from around Sano-city · Sweets of Sano ·</textPath>
    </text>
  </svg>
  <div class="ornament front__scene" role="img" aria-label="山の上の砦跡と湧水の風景イラスト"></div>
  <span class="vertical front__title-sub">ひなた</span>
  <span class="vertical front__title-main">夢みる</span>
  <span class="vertical front__title-bar">バー</span>
  <div class="front__badge" role="img" aria-label="郷土愛マークの位置"></div>
  <div class="front__flavor">あずき味</div>
  <div class="ornament front__wave" role="img" aria-label="波と雲の文様"></div>
  <p class="front__tagline">Sweets from around Sano-city</p>
  <div class="front__region">佐野の恵み</div>
</section>

<!-- back, single colour -->
<section class="pack pack--mono back" style="left:383px; top:14px;">
  <div class="pack__frame"></div>
  <div class="ornament back__cloud-top" role="img" aria-label="雲文様の帯"></div>
  <div class="ornament back__mark" role="img" aria-label="小さな飾り紋"></div>
  <div class="back__seal" role="img" aria-label="郷土愛マークの位置"></div>
  <span class="vertical back__logo-sub">ひなた</span>
  <span class="vertical back__logo-main">夢みるバー</span>
  <div class="back__stamp"></div>
  <div class="back__label">
    <p class="back__label-kind">【菓類別】</p>
    <p class="back__label-name">氷菓</p>
    <p>【ヒナタユメミルバー】</p>
    <p>名称 氷菓 原材料名 小豆 砂糖 牛乳</p>
    <p>内容量 80ml 保存方法 −18℃以下</p>
    <p>製造者 朝霧屋 佐野市本町一丁目</p>
  </div>
  <div class="ornament back__stick" role="img" aria-label="アイスキャンディーの図"></div>
  <div class="ornament back__cloud-bottom" role="img" aria-label="雲文様の帯"></div>
</section>

<!-- front, tinted -->
<section class="pack pack--rose front" style="left:45px; top:650px;">
  <div class="pack__frame"></div>
  <div class="ornament front__corner" style="left:18px; top:18px;" role="img" aria-label="角の飾り"></div>
  <div class="ornament front__corner" style="right:18px; top:18px;" role="img" aria-label="角の飾り"></div>
  <div class="front__maker">味噌まんじゅう朝霧屋</div>
  <div class="ornament front__cloud-row" role="img" aria-label="雲文様の帯"></div>
  <svg class="front__medal" viewBox="0 0 220 220" aria-hidden="true">
    <defs><path id="arcB" d="M110,110 m-97,0 a97,97 0 1,1 194,0 a97,97 0 1,1 -194,0"/></defs>
    <circle cx="110" cy="110" r="105" fill="none" stroke="currentColor" stroke-width="1.5"/>
    <circle cx="110" cy="110" r="88" fill="none" stroke="currentColor" stroke-width="1"/>
    <text font-size="8" fill="currentColor" font-family="Noto Serif JP, serif" letter-spacing="1">
      <textPath href="#arcB">Ice candy with milk and fruit from around Sano-city · Sweets of Sano ·</textPath>
    </text>
  </svg>
  <div class="ornament front__scene" role="img" aria-label="山の上の砦跡と湧水の風景イラスト"></div>
  <span class="vertical front__title-sub">ひなた</span>
  <span class="vertical front__title-main">夢みる</span>
  <span class="vertical front__title-bar">バー</span>
  <div class="front__badge" role="img" aria-label="郷土愛マークの位置"></div>
  <div class="front__flavor">あずき味</div>
  <div class="ornament front__wave" role="img" aria-label="波と雲の文様"></div>
  <p class="front__tagline">Sweets from around Sano-city</p>
  <div class="front__region">佐野の恵み</div>
</section>

<!-- back, tinted -->
<section class="pack pack--rose back" style="left:383px; top:650px;">
  <div class="pack__frame"></div>
  <div class="ornament back__cloud-top" role="img" aria-label="雲文様の帯"></div>
  <div class="ornament back__mark" role="img" aria-label="小さな飾り紋"></div>
  <div class="back__seal" role="img" aria-label="郷土愛マークの位置"></div>
  <span class="vertical back__logo-sub">ひなた</span>
  <span class="vertical back__logo-main">夢みるバー</span>
  <div class="back__stamp"></div>
  <div class="back__label">
    <p class="back__label-kind">【菓類別】</p>
    <p class="back__label-name">氷菓</p>
    <p>【ヒナタユメミルバー】</p>
    <p>名称 氷菓 原材料名 小豆 砂糖 牛乳</p>
    <p>内容量 80ml 保存方法 −18℃以下</p>
    <p>製造者 朝霧屋 佐野市本町一丁目</p>
  </div>
  <div class="ornament back__stick" role="img" aria-label="アイスキャンディーの図"></div>
  <div class="ornament back__cloud-bottom" role="img" aria-label="雲文様の帯"></div>
</section>

</body>
</html>
```